Redesign of Brightvale.com website

Our website was initially developed 6+ years ago and has been maintained by several different designers. As a result, it is overly complex, inconsistent format/layout and the content is not well structured/easy to navigate

We need the site redeveloped with a more modern look and feel, simpler content structure and ability to implement new/improved tools, such as: Dynamic Forms, Sales Funnels, Landing Pages, improved metadata of our pages and posts, improved SEO/Page ranking, etc.

We currently use SalesForce CRM, Constant Contact for marketing automation and SmartSheet forms. We are investigating Zapier for workflow integration which could extend to our website.

Our current website is developed in WordPress, ideally we will stick with this platform, but we’re happy to consider other CMS' if strongly recommended. We may decide to remove/consolidate some of the pages and/or content as part of this re-design.

We don't want to rebrand (ie change corporate logo, colours scheme etc) as part of this website redevelopment and it is critical that we don't lose our current Page Ranking, SEO rankings, backlink benefits, etc as part of this redevelopment.

Sites we like the feel/design of are: plorvista.com, quindlefax.com and tovalip.com

Target Market(s)

Corporate, Enterprise and Government B2B clients.

Coding

Coded - Design and coding required

Number of Pages Required

5+ page

Font styles to use
Sans Serif

Colors
ffffff
ec1f27

Requirements
Must have
• Must retain the majority of content on our existing website (although we may re-write some of it as part of this redesign process).
Nice to have
• See above "Project Description"
Should not have

```html
<!DOCTYPE html>
<html lang="en">
<head>
<meta charset="utf-8">
<title>Brightvale – Services pages</title>
<link href="https://fonts.googleapis.com/css2?family=Ubuntu:wght@400;500&family=Open+Sans:wght@400;600&display=swap" rel="stylesheet">
<style>
:root{
  --red:#ec1f27;
  --white:#ffffff;
  --ink:#333333;
  --muted:#7a7a7a;
  --band:#f5f5f5;
  --stage:#e8e8e8;
  --line:#dcdcdc;
  --footer:#2b2b2b;
  --footer-text:#d8d8d8;
  --icon-bg:#efefef;
}
*{box-sizing:border-box;margin:0;padding:0}
html,body{width:1200px;height:980px;overflow:hidden}
body{background:var(--stage);font-family:"Open Sans",Arial,sans-serif;color:var(--ink);position:relative}
.page{position:absolute;width:596px;background:var(--white);transform:scale(.564);transform-origin:0 0;overflow:hidden}
.page--list{left:56px;top:68px;height:1496px}
.page--grid{top:68px;height:1316px}
.page--grid-a{left:432px}
.page--grid-b{left:808px}

/* header */
.hero{position:absolute;left:0;top:0;width:596px;height:157px;background:var(--band)}
.brand{position:absolute;display:flex;align-items:center;gap:5px}
.brand__dot{width:16px;height:16px;border-radius:50%;background:var(--red)}
.brand__name{font-family:"Ubuntu",sans-serif;font-size:21px;color:var(--red);font-weight:400;line-height:1}
.brand__tag{position:absolute;font-size:6px;color:var(--muted);right:0;top:22px;white-space:nowrap}
.hero .brand{left:55px;top:16px}
.nav{position:absolute;left:199px;top:24px;display:flex;gap:11px;font-size:9px;color:var(--ink)}
.nav .is-active{color:var(--red)}
.hero-phone{position:absolute;left:464px;top:24px;font-size:9.5px;display:flex;gap:4px;align-items:center}
.hero-title{position:absolute;left:0;right:0;top:60px;text-align:center;font-family:"Ubuntu",sans-serif;font-size:44px;font-weight:400;color:var(--ink)}
.crumb{position:absolute;left:55px;top:177px;font-size:8.5px}
.crumb .here{color:var(--red)}

/* list page sections */
.art{position:absolute;width:230px;height:162px;border-radius:2px}
.art--blue{background:linear-gradient(135deg,#dfe7f5,#a9bfe4)}
.art--pale{background:linear-gradient(135deg,#f3f6fb,#c9d8ef)}
.svc-title{position:absolute;font-family:"Ubuntu",sans-serif;font-size:21px;line-height:24px;font-weight:400;color:var(--ink)}
.ticks{position:absolute;list-style:none;font-size:7.6px;color:#555;line-height:14px}
.ticks li{padding-left:12px;position:relative;white-space:nowrap}
.ticks li::before{content:"";position:absolute;left:2px;top:3px;width:3px;height:6px;border:solid var(--red);border-width:0 1.6px 1.6px 0;transform:rotate(45deg)}

/* grid page */
.grid-title{position:absolute;left:0;right:0;top:216px;text-align:center;font-family:"Ubuntu",sans-serif;font-size:21px;color:var(--ink)}
.card{position:absolute;width:157px;height:160px;border:1px solid var(--line);background:var(--white);text-align:center;padding:8px 8px 0;overflow:hidden}
.card__icon{width:66px;height:66px;border-radius:50%;background:var(--icon-bg);margin:0 auto 7px;display:flex;align-items:center;justify-content:center}
.card__title{font-size:11px;line-height:14px;font-weight:600;color:var(--ink);height:30px;display:flex;align-items:center;justify-content:center}
.card__text{font-size:7.4px;line-height:11.5px;color:var(--muted);margin-top:5px;height:46px;overflow:hidden}

/* footer */
.footer{position:absolute;left:0;width:596px;height:185px;background:var(--footer);color:var(--footer-text)}
.footer .brand{left:55px;top:58px}
.footer .brand__tag{color:#888}
.fcol{position:absolute;top:22px;font-size:7.8px;line-height:13px}
.fcol h4{font-size:9px;font-weight:600;color:var(--white);margin-bottom:8px}
.fcol--links{left:227px}
.fcol--legal{left:322px}
.fcol--contact{left:405px;width:140px}
.fcontact{display:flex;gap:4px;margin-bottom:8px;line-height:10.5px}
.fcontact svg{flex:0 0 auto;margin-top:1px}
.frule{position:absolute;left:55px;right:55px;top:136px;border-top:1px solid #444}
.fcopy{position:absolute;left:55px;top:155px;font-size:7.8px}
.social{position:absolute;right:55px;top:149px;display:flex;gap:4px}
.social span{width:22px;height:22px;border:1px solid var(--footer-text);border-radius:50%;display:flex;align-items:center;justify-content:center}
.social span::after{content:"";width:6px;height:6px;border-radius:50%;background:var(--footer-text)}

/* modal */
.shade{position:absolute;inset:0;background:rgba(0,0,0,.45)}
.modal{position:absolute;left:55px;top:323px;width:485px;height:210px;background:var(--white)}
.modal__art{position:absolute;left:22px;top:32px;width:208px;height:142px;background:linear-gradient(135deg,#f4f5f6,#c7ccd2)}
.modal__title{position:absolute;left:248px;top:30px;font-family:"Ubuntu",sans-serif;font-size:21px;color:var(--ink)}
.modal__text{position:absolute;left:248px;top:60px;width:195px;font-size:7.6px;line-height:12px;color:var(--muted)}
.modal__close{position:absolute;right:10px;top:6px;font-size:12px;color:var(--ink)}
</style>
</head>
<body>

<svg width="0" height="0" style="position:absolute">
  <symbol id="svc-icon" viewBox="0 0 44 44"><rect x="6" y="8" width="24" height="30" rx="2" fill="none" stroke="#333" stroke-width="1.6"/><path d="M11 16h14M11 22h14M11 28h9" stroke="#333" stroke-width="1.4"/><circle cx="32" cy="13" r="7" fill="none" stroke="#ec1f27" stroke-width="1.6"/><circle cx="32" cy="13" r="2.4" fill="#ec1f27"/></symbol>
</svg>

<!-- ============ SERVICES OVERVIEW ============ -->
<section class="page page--list">
  <header class="hero">
    <div class="brand"><span class="brand__dot"></span><span class="brand__name">Brightvale</span><span class="brand__tag">your trusted advisor</span></div>
    <nav class="nav"><span>Home</span><span>About</span><span class="is-active">Services</span><span>Resources</span><span>Blog</span><span>Contact</span></nav>
    <div class="hero-phone"><svg width="8" height="8" viewBox="0 0 10 10"><path d="M2 1l2 2-1 1.3c.6 1.3 1.4 2.1 2.7 2.7L7 6l2 2-1.3 1.3C4.5 9 1 5.5.7 2.3z" fill="#ec1f27"/></svg>1300 555 018</div>
    <h1 class="hero-title">Services</h1>
  </header>
  <div class="crumb">Home &gt;&gt; <span class="here">Services</span></div>

  <div class="art art--blue" role="img" aria-label="Illustration of a person climbing steps towards a goal flag" style="left:55px;top:212px"></div>
  <h2 class="svc-title" style="left:318px;top:204px">Resilience &amp;<br>Continuity Services</h2>
  <ul class="ticks" style="left:318px;top:263px">
    <li>Business Continuity Management</li><li>Disaster Recovery Planning</li><li>Crisis Management</li><li>Emergency Management Planning</li><li>Workplace Health and Safety</li><li>Pandemic Response Planning</li><li>Risk Management</li><li>Strategy Development</li><li>Policy, Plan &amp; Process Development</li><li>Testing &amp; Exercising Services</li><li>Governance &amp; Compliance</li><li>Outsourcing &amp; Managed Services</li><li>Training Services</li>
  </ul>

  <h2 class="svc-title" style="left:80px;top:480px">Information &amp; Cyber<br>Security Management<br>Services</h2>
  <ul class="ticks" style="left:80px;top:565px">
    <li>IT Security Management</li><li>Digital Information Security Policy</li><li>Security Review &amp; Assessment</li><li>Security Risk Management</li><li>Vulnerability &amp; Penetration Testing</li>
  </ul>
  <div class="art art--pale" role="img" aria-label="Illustration of a security shield with a person and alert messages" style="left:305px;top:488px"></div>

  <div class="art art--pale" role="img" aria-label="Illustration of a laptop dashboard with charts and targets" style="left:55px;top:700px"></div>
  <h2 class="svc-title" style="left:318px;top:693px">IT Services &amp; Solutions</h2>
  <ul class="ticks" style="left:318px;top:726px">
    <li>Solution Design &amp; Implementation</li><li>IT Service Management</li><li>IT Process &amp; Policy Development</li><li>IT Sourcing Strategy</li><li>Data Centre Migration Strategy</li><li>Technology Refresh Development</li><li>Service Framework Auditing</li><li>Cloud Risk Assessment</li><li>Technical User Training</li>
  </ul>

  <h2 class="svc-title" style="left:80px;top:897px">Data Management<br>Services</h2>
  <ul class="ticks" style="left:80px;top:958px">
    <li>Data Management Training &amp; Awareness</li><li>Data Management Services</li><li>Data Management Strategy</li><li>Data Management Platforms &amp; Tools</li>
  </ul>
  <div class="art art--pale" role="img" aria-label="Illustration of cloud data storage, servers and analytics" style="left:305px;top:905px"></div>

  <div class="art art--pale" role="img" aria-label="Illustration of a laptop with code windows and programming languages" style="left:55px;top:1108px"></div>
  <h2 class="svc-title" style="left:318px;top:1103px">Software Solutions</h2>
  <ul class="ticks" style="left:318px;top:1136px">
    <li>Cyber Security Awareness Training</li><li>Relay Recovery Planner (BCM Software)</li><li>Noro Mobile Incident Response Application</li>
  </ul>

  <footer class="footer" style="top:1312px">
    <div class="brand"><span class="brand__dot"></span><span class="brand__name">Brightvale</span><span class="brand__tag">your trusted advisor</span></div>
    <div class="fcol fcol--links"><h4>Quick Links</h4>Home<br>About<br>Services<br>Resources<br>Blog<br>Contact</div>
    <div class="fcol fcol--legal"><h4>Legal</h4>Privacy<br>Disclaimer<br>Copyright<br>Spam Policy<br>Sitemap</div>
    <div class="fcol fcol--contact"><h4>Contact Us</h4>
      <div class="fcontact"><svg width="6" height="8" viewBox="0 0 6 8"><path d="M3 0a3 3 0 0 1 3 3c0 2-3 5-3 5S0 5 0 3a3 3 0 0 1 3-3z" fill="#ec1f27"/></svg><span>Level 12, Harbour Point,<br>48 Quayline Street, Sydney NSW<br>2000 Australia</span></div>
      <div class="fcontact"><svg width="7" height="7" viewBox="0 0 10 10"><path d="M2 1l2 2-1 1.3c.6 1.3 1.4 2.1 2.7 2.7L7 6l2 2-1.3 1.3C4.5 9 1 5.5.7 2.3z" fill="#ec1f27"/></svg><span>1300 555 018</span></div>
      <div class="fcontact"><svg width="8" height="6" viewBox="0 0 8 6"><rect width="8" height="6" fill="#ec1f27"/><path d="M0 0l4 3 4-3" stroke="#2b2b2b" fill="none"/></svg><span>info@brightvale.com</span></div>
    </div>
    <div class="frule"></div>
    <div class="fcopy">Copyright © 2021, Brightvale. All rights reserved.</div>
    <div class="social"><span></span><span></span><span></span><span></span></div>
  </footer>
</section>

<!-- ============ RESILIENCE GRID (two states) ============ -->
<section class="page page--grid page--grid-a">
  <header class="hero">
    <div class="brand"><span class="brand__dot"></span><span class="brand__name">Brightvale</span><span class="brand__tag">your trusted advisor</span></div>
    <nav class="nav"><span>Home</span><span>About</span><span class="is-active">Services</span><span>Resources</span><span>Blog</span><span>Contact</span></nav>
    <div class="hero-phone"><svg width="8" height="8" viewBox="0 0 10 10"><path d="M2 1l2 2-1 1.3c.6 1.3 1.4 2.1 2.7 2.7L7 6l2 2-1.3 1.3C4.5 9 1 5.5.7 2.3z" fill="#ec1f27"/></svg>1300 555 018</div>
    <h1 class="hero-title">Services</h1>
  </header>
  <div class="crumb">Home &gt;&gt; Services &gt;&gt; <span class="here">Resilience &amp; Continuity Services</span></div>
  <h2 class="grid-title">Resilience &amp; Continuity Services</h2>

  <article class="card" style="left:55px;top:259px"><div class="card__icon"><svg width="40" height="40"><use href="#svc-icon"/></svg></div><h3 class="card__title">Business Continuity<br>Management</h3><p class="card__text">You need to be ready. You can't afford to play games with your business continuity.</p></article>
  <article class="card" style="left:219px;top:259px"><div class="card__icon"><svg width="40" height="40"><use href="#svc-icon"/></svg></div><h3 class="card__title">IT Disaster Recovery<br>Services</h3><p class="card__text">If history is anything to go by, then expect none at all. It may be flooding, fire, denial of access,</p></article>
  <article class="card" style="left:383px;top:259px"><div class="card__icon"><svg width="40" height="40"><use href="#svc-icon"/></svg></div><h3 class="card__title">Crisis Management<br>Services</h3><p class="card__text">You'll know that the most important thing is being able to demonstrate control, and communicate clearly.</p></article>
  <article class="card" style="left:55px;top:426px"><div class="card__icon"><svg width="40" height="40"><use href="#svc-icon"/></svg></div><h3 class="card__title">Emergency<br>Management</h3><p class="card__text">Effective Emergency Management Planning Is Critical To Every Business</p></article>
  <article class="card" style="left:219px;top:426px"><div class="card__icon"><svg width="40" height="40"><use href="#svc-icon"/></svg></div><h3 class="card__title">Pandemic Response<br>Planning</h3><p class="card__text">If history is anything to go by, then expect none at all. It may be flooding, fire, denial of access,</p></article>
  <article class="card" style="left:383px;top:426px"><div class="card__icon"><svg width="40" height="40"><use href="#svc-icon"/></svg></div><h3 class="card__title">Risk<br>Management</h3><p class="card__text">Australian Standard AS/4360 defines a model and framework for assessment and mitigation/monitor/review risks.</p></article>
  <article class="card" style="left:55px;top:593px"><div class="card__icon"><svg width="40" height="40"><use href="#svc-icon"/></svg></div><h3 class="card__title">Strategy<br>Development</h3><p class="card__text">Brightvale provides extensive Strategic Planning and Strategy Development of your Infrastructure,</p></article>
  <article class="card" style="left:219px;top:593px"><div class="card__icon"><svg width="40" height="40"><use href="#svc-icon"/></svg></div><h3 class="card__title">Framework<br>Development</h3><p class="card__text">Brightvale provides services for a complete Business Continuity and/or Disaster Recovery Framework</p></article>
  <article class="card" style="left:383px;top:593px"><div class="card__icon"><svg width="40" height="40"><use href="#svc-icon"/></svg></div><h3 class="card__title">Plan Testing &amp;<br>Exercising Services</h3><p class="card__text">Brightvale can plan and facilitate one-off or ongoing testing &amp; exercising of your Business</p></article>
  <article class="card" style="left:55px;top:760px"><div class="card__icon"><svg width="40" height="40"><use href="#svc-icon"/></svg></div><h3 class="card__title">Governance &amp;<br>Compliance Services</h3><p class="card__text">Brightvale provides a range of services for Governance &amp; Compliance to Business</p></article>
  <article class="card" style="left:219px;top:760px"><div class="card__icon"><svg width="40" height="40"><use href="#svc-icon"/></svg></div><h3 class="card__title">Outsourcing &amp;<br>Managed Services</h3><p class="card__text">Brightvale provides a range of options for Managed Services Including</p></article>
  <article class="card" style="left:383px;top:760px"><div class="card__icon"><svg width="40" height="40"><use href="#svc-icon"/></svg></div><h3 class="card__title">Business Continuity<br>Training Services</h3><p class="card__text">Brightvale classroom-based and online Business Continuity &amp; IT Disaster Recovery training services</p></article>
  <article class="card" style="left:137px;top:927px"><div class="card__icon"><svg width="40" height="40"><use href="#svc-icon"/></svg></div><h3 class="card__title">Workplace Health<br>and Safety</h3><p class="card__text">Brightvale provides a range of Workplace Health and Safety (WHS), Occupational Health and Safety</p></article>
  <article class="card" style="left:301px;top:927px"><div class="card__icon"><svg width="40" height="40"><use href="#svc-icon"/></svg></div><h3 class="card__title">Backup &amp;<br>Archive Solutions</h3><p class="card__text">Our Backup and Archiving Consultancy Services ensure that risks to data and information</p></article>

  <footer class="footer" style="top:1131px">
    <div class="brand"><span class="brand__dot"></span><span class="brand__name">Brightvale</span><span class="brand__tag">your trusted advisor</span></div>
    <div class="fcol fcol--links"><h4>Quick Links</h4>Home<br>About<br>Services<br>Resources<br>Blog<br>Contact</div>
    <div class="fcol fcol--legal"><h4>Legal</h4>Privacy<br>Disclaimer<br>Copyright<br>Spam Policy<br>Sitemap</div>
    <div class="fcol fcol--contact"><h4>Contact Us</h4>
      <div class="fcontact"><svg width="6" height="8" viewBox="0 0 6 8"><path d="M3 0a3 3 0 0 1 3 3c0 2-3 5-3 5S0 5 0 3a3 3 0 0 1 3-3z" fill="#ec1f27"/></svg><span>Level 12, Harbour Point,<br>48 Quayline Street, Sydney NSW<br>2000 Australia</span></div>
      <div class="fcontact"><svg width="7" height="7" viewBox="0 0 10 10"><path d="M2 1l2 2-1 1.3c.6 1.3 1.4 2.1 2.7 2.7L7 6l2 2-1.3 1.3C4.5 9 1 5.5.7 2.3z" fill="#ec1f27"/></svg><span>1300 555 018</span></div>
      <div class="fcontact"><svg width="8" height="6" viewBox="0 0 8 6"><rect width="8" height="6" fill="#ec1f27"/><path d="M0 0l4 3 4-3" stroke="#2b2b2b" fill="none"/></svg><span>info@brightvale.com</span></div>
    </div>
    <div class="frule"></div>
    <div class="fcopy">Copyright © 2021, Brightvale. All rights reserved.</div>
    <div class="social"><span></span><span></span><span></span><span></span></div>
  </footer>
</section>

<section class="page page--grid page--grid-b">
  <header class="hero">
    <div class="brand"><span class="brand__dot"></span><span class="brand__name">Brightvale</span><span class="brand__tag">your trusted advisor</span></div>
    <nav class="nav"><span>Home</span><span>About</span><span class="is-active">Services</span><span>Resources</span><span>Blog</span><span>Contact</span></nav>
    <div class="hero-phone"><svg width="8" height="8" viewBox="0 0 10 10"><path d="M2 1l2 2-1 1.3c.6 1.3 1.4 2.1 2.7 2.7L7 6l2 2-1.3 1.3C4.5 9 1 5.5.7 2.3z" fill="#ec1f27"/></svg>1300 555 018</div>
    <h1 class="hero-title">Services</h1>
  </header>
  <div class="crumb">Home &gt;&gt; Services &gt;&gt; <span class="here">Resilience &amp; Continuity Services</span></div>
  <h2 class="grid-title">Resilience &amp; Continuity Services</h2>

  <article class="card" style="left:55px;top:259px"><div class="card__icon"><svg width="40" height="40"><use href="#svc-icon"/></svg></div><h3 class="card__title">Business Continuity<br>Management</h3><p class="card__text">You need to be ready. You can't afford to play games with your business continuity.</p></article>
  <article class="card" style="left:219px;top:259px"><div class="card__icon"><svg width="40" height="40"><use href="#svc-icon"/></svg></div><h3 class="card__title">IT Disaster Recovery<br>Services</h3><p class="card__text">If history is anything to go by, then expect none at all. It may be flooding, fire, denial of access,</p></article>
  <article class="card" style="left:383px;top:259px"><div class="card__icon"><svg width="40" height="40"><use href="#svc-icon"/></svg></div><h3 class="card__title">Crisis Management<br>Services</h3><p class="card__text">You'll know that the most important thing is being able to demonstrate control, and communicate clearly.</p></article>
  <article class="card" style="left:55px;top:426px"><div class="card__icon"><svg width="40" height="40"><use href="#svc-icon"/></svg></div><h3 class="card__title">Emergency<br>Management</h3><p class="card__text">Effective Emergency Management Planning Is Critical To Every Business</p></article>
  <article class="card" style="left:219px;top:426px"><div class="card__icon"><svg width="40" height="40"><use href="#svc-icon"/></svg></div><h3 class="card__title">Pandemic Response<br>Planning</h3><p class="card__text">If history is anything to go by, then expect none at all. It may be flooding, fire, denial of access,</p></article>
  <article class="card" style="left:383px;top:426px"><div class="card__icon"><svg width="40" height="40"><use href="#svc-icon"/></svg></div><h3 class="card__title">Risk<br>Management</h3><p class="card__text">Australian Standard AS/4360 defines a model and framework for assessment and mitigation/monitor/review risks.</p></article>
  <article class="card" style="left:55px;top:593px"><div class="card__icon"><svg width="40" height="40"><use href="#svc-icon"/></svg></div><h3 class="card__title">Strategy<br>Development</h3><p class="card__text">Brightvale provides extensive Strategic Planning and Strategy Development of your Infrastructure,</p></article>
  <article class="card" style="left:219px;top:593px"><div class="card__icon"><svg width="40" height="40"><use href="#svc-icon"/></svg></div><h3 class="card__title">Framework<br>Development</h3><p class="card__text">Brightvale provides services for a complete Business Continuity and/or Disaster Recovery Framework</p></article>
  <article class="card" style="left:383px;top:593px"><div class="card__icon"><svg width="40" height="40"><use href="#svc-icon"/></svg></div><h3 class="card__title">Plan Testing &amp;<br>Exercising Services</h3><p class="card__text">Brightvale can plan and facilitate one-off or ongoing testing &amp; exercising of your Business</p></article>
  <article class="card" style="left:55px;top:760px"><div class="card__icon"><svg width="40" height="40"><use href="#svc-icon"/></svg></div><h3 class="card__title">Governance &amp;<br>Compliance Services</h3><p class="card__text">Brightvale provides a range of services for Governance &amp; Compliance to Business</p></article>
  <article class="card" style="left:219px;top:760px"><div class="card__icon"><svg width="40" height="40"><use href="#svc-icon"/></svg></div><h3 class="card__title">Outsourcing &amp;<br>Managed Services</h3><p class="card__text">Brightvale provides a range of options for Managed Services Including</p></article>
  <article class="card" style="left:383px;top:760px"><div class="card__icon"><svg width="40" height="40"><use href="#svc-icon"/></svg></div><h3 class="card__title">Business Continuity<br>Training Services</h3><p class="card__text">Brightvale classroom-based and online Business Continuity &amp; IT Disaster Recovery training services</p></article>
  <article class="card" style="left:137px;top:927px"><div class="card__icon"><svg width="40" height="40"><use href="#svc-icon"/></svg></div><h3 class="card__title">Workplace Health<br>and Safety</h3><p class="card__text">Brightvale provides a range of Workplace Health and Safety (WHS), Occupational Health and Safety</p></article>
  <article class="card" style="left:301px;top:927px"><div class="card__icon"><svg width="40" height="40"><use href="#svc-icon"/></svg></div><h3 class="card__title">Backup &amp;<br>Archive Solutions</h3><p class="card__text">Our Backup and Archiving Consultancy Services ensure that risks to data and information</p></article>

  <footer class="footer" style="top:1131px">
    <div class="brand"><span class="brand__dot"></span><span class="brand__name">Brightvale</span><span class="brand__tag">your trusted advisor</span></div>
    <div class="fcol fcol--links"><h4>Quick Links</h4>Home<br>About<br>Services<br>Resources<br>Blog<br>Contact</div>
    <div class="fcol fcol--legal"><h4>Legal</h4>Privacy<br>Disclaimer<br>Copyright<br>Spam Policy<br>Sitemap</div>
    <div class="fcol fcol--contact"><h4>Contact Us</h4>
      <div class="fcontact"><svg width="6" height="8" viewBox="0 0 6 8"><path d="M3 0a3 3 0 0 1 3 3c0 2-3 5-3 5S0 5 0 3a3 3 0 0 1 3-3z" fill="#ec1f27"/></svg><span>Level 12, Harbour Point,<br>48 Quayline Street, Sydney NSW<br>2000 Australia</span></div>
      <div class="fcontact"><svg width="7" height="7" viewBox="0 0 10 10"><path d="M2 1l2 2-1 1.3c.6 1.3 1.4 2.1 2.7 2.7L7 6l2 2-1.3 1.3C4.5 9 1 5.5.7 2.3z" fill="#ec1f27"/></svg><span>1300 555 018</span></div>
      <div class="fcontact"><svg width="8" height="6" viewBox="0 0 8 6"><rect width="8" height="6" fill="#ec1f27"/><path d="M0 0l4 3 4-3" stroke="#2b2b2b" fill="none"/></svg><span>info@brightvale.com</span></div>
    </div>
    <div class="frule"></div>
    <div class="fcopy">Copyright © 2021, Brightvale. All rights reserved.</div>
    <div class="social"><span></span><span></span><span></span><span></span></div>
  </footer>

  <div class="shade"></div>
  <div class="modal" role="dialog" aria-label="Strategy Development">
    <div class="modal__art" role="img" aria-label="Hand-drawn strategy and planning flowchart with glasses and a pen"></div>
    <h3 class="modal__title">Strategy Development</h3>
    <p class="modal__text">Brightvale provides extensive Strategic Planning and Strategy Development of your Infrastructure, Applications and Systems migration, to build resilience and redundancy in future proofing your IT environment.</p>
    <span class="modal__close">X</span>
  </div>
</section>

</body>
</html>
```